Quillfern Litigation Funding Letterhead & Document Template

We need a letter head designed for our fund. Our fund works with law firms and investors across the globe. We need a a cover letter template as well as a document template for subsequent pages. Blue and white color scheme is preferred. This is our predecessor's website: https://www.quillfernlc.com/index.html. Please see our logo attached. The logo color code is #19478d. Font is Gotham-Medium.
Target Market(s)
Sophisticated investors and law firms
Font styles to use
Sans Serif
Colors
0255a3

```html
<!DOCTYPE html>
<html lang="en">
<head>
<meta charset="utf-8">
<title>Quillfern Litigation Funding – Stationery</title>
<link rel="stylesheet" href="https://fonts.googleapis.com/css2?family=Lato:wght@400;700&family=Montserrat:wght@600&family=Open+Sans:wght@400;600&display=swap">
<style>
  :root {
    --board: #3d3d3d;
    --label: #dcdcdc;
    --paper: #ffffff;
    --brand: #1c4795;
    --ink: #222222;
    --body-ink: #3a3a3a;
    --ghost: #ebebf4;
  }
  * { box-sizing: border-box; margin: 0; padding: 0; }
  html, body { width: 1200px; height: 918px; overflow: hidden; background: var(--board); }
  .board { position: relative; width: 1200px; height: 918px; }
  .sheet-label {
    position: absolute; top: 96px; width: 300px; text-align: center;
    font: 600 24px/1.3 "Open Sans", sans-serif; color: var(--label);
  }
  .sheet {
    position: absolute; top: 152px; width: 435px; height: 614px;
    background: var(--paper); box-shadow: 0 10px 22px rgba(0,0,0,.45);
    font-family: "Lato", sans-serif; color: var(--ink);
  }
  .cover { left: 148px; }
  .letterhead { left: 612px; }

  .wordmark {
    position: absolute; font: 600 8px/1.25 "Montserrat", sans-serif;
    color: var(--brand); letter-spacing: .3px; text-align: center;
  }
  .wordmark .mark { display: block; width: 20px; height: 20px; margin: 0 auto 6px; background: var(--brand); }
  .cover .wordmark { left: 0; right: 0; top: 16px; }
  .letterhead .wordmark { left: 30px; width: 102px; top: 22px; font-size: 7.2px; }

  .cover .rule { position: absolute; left: 31px; right: 30px; top: 69px; border-top: 1px solid var(--brand); }
  .contact-row {
    position: absolute; top: 75px; left: 0; right: 0; text-align: center;
    font: 400 8.3px/12px "Open Sans", sans-serif; color: var(--ink);
  }
  .contact-row .sep { color: var(--brand); margin: 0 4px; }
  .icon { display: inline-block; width: 7px; height: 7px; vertical-align: -1px; margin-right: 2px; }

  .letter { position: absolute; left: 43px; width: 353px; }
  .salutation { top: 188px; font-size: 10px; }
  .date { top: 224px; font-size: 8.8px; }
  .body-copy { top: 261px; font-size: 7.9px; letter-spacing: .12px; line-height: 10.2px; color: var(--body-ink); text-align: justify; }
  .body-copy p + p { margin-top: 10.2px; }
  .closing { top: 464px; font-size: 8.6px; }

  .contact-block {
    position: absolute; top: 36px; font: 400 8.3px/10px "Open Sans", sans-serif; color: var(--ink);
    border-left: 1.5px solid var(--brand); padding-left: 6px;
  }
  .contact-block.phones { left: 215px; }
  .contact-block.web { left: 297px; }

  .ghost-name {
    position: absolute; left: 0; right: 0; top: 268px; text-align: center;
    font: 600 26px/1.25 "Montserrat", sans-serif; color: var(--ghost);
  }

  .footer-band { position: absolute; left: 0; right: 0; top: 586px; height: 14px; }
  .footer-band .band-main {
    position: absolute; left: 0; width: 388px; height: 14px; background: var(--brand);
    clip-path: polygon(0 0, 100% 0, calc(100% - 9px) 100%, 0 100%);
    font: 600 8px/14px "Open Sans", sans-serif; color: #fff; padding-left: 30px; white-space: nowrap;
  }
  .footer-band .band-mark { position: absolute; left: 396px; top: 2px; width: 10px; height: 10px; background: var(--brand); }
  .footer-band .band-end { position: absolute; left: 413px; right: 0; height: 14px; background: var(--brand); }
</style>
</head>
<body>
<div class="board">
  <h2 class="sheet-label" style="left:215px">Cover Letter</h2>
  <h2 class="sheet-label" style="left:670px">Letterhead</h2>

  <section class="sheet cover">
    <div class="wordmark"><span class="mark"></span>QUILLFERN LITIGATION<br>FUNDING</div>
    <div class="rule"></div>
    <div class="contact-row">
      <svg class="icon" viewBox="0 0 10 10"><path d="M2 0.5 L4 3 L3 4 Q4.5 6 6 7 L7 6 L9.5 8 L8 9.5 Q3 9 0.5 2 Z" fill="#1c4795"/></svg>(555) 214-7200<span class="sep">|</span><svg class="icon" viewBox="0 0 10 10"><rect x="0.5" y="2" width="9" height="6" fill="#1c4795"/><path d="M0.5 2 L5 5.5 L9.5 2" stroke="#fff" fill="none"/></svg>info@quillfernlc.com<span class="sep">|</span><svg class="icon" viewBox="0 0 10 10"><circle cx="5" cy="5" r="4.5" fill="#1c4795"/><path d="M0.5 5 H9.5 M5 0.5 V9.5" stroke="#fff" stroke-width=".7"/></svg>www.quillfernlc.com
    </div>

    <p class="letter salutation">Dear Martin</p>
    <p class="letter date">Date : 01 May 2020</p>
    <div class="letter body-copy">
      <p>Lorem ipsum dolor sit amet, consectetur adipisicing elit, sed do eiusmod tempor incididunt ut labore et dolore magna aliqua. Ut enim ad minim veniam, quis nostrud exercitation ullamco laboris nisi ut aliquip ex ea commodo consequat. Duis aute irure dolor in reprehenderit in voluptate velit esse cillum dolore eu fugiat nulla pariatur. Excepteur sint occaecat cupidatat non proident, sunt in culpa qui officia deserunt mollit anim id est laborum. re et dolore magnam aliquam quaerat voluptatem.</p>
      <p>Lorem ipsum dolor sit amet, consectetur adipisicing elit, sed do eiusmod tempor incididunt ut labore et dolore magna aliqua. Ut enim ad minim veniam, quis nostrud exercitation ullamco laboris nisi ut aliquip ex ea commodo consequat. Duis aute irure dolor in reprehenderit in voluptate velit esse cillum dolore eu fugiat nulla pariatur. Excepteur sint occaecat cupidatat non proident, sunt in culpa qui officia deserunt mollit anim id est laborum. re et dolore magnam aliquam quaerat voluptatem.</p>
      <p>Lorem ipsum dolor sit amet, consectetur adipisicing elit, sed do eiusmod tempor incididunt ut labore et dolore magna aliqua. Ut enim ad minim veniam, quis nostrud exercitation ullamco laboris nisi ut aliquip ex ea commodo consequat.</p>
    </div>
    <p class="letter closing">Regards</p>
  </section>

  <section class="sheet letterhead">
    <div class="wordmark"><span class="mark"></span>QUILLFERN LITIGATION<br>FUNDING</div>
    <div class="contact-block phones">
      <div><svg class="icon" viewBox="0 0 10 10"><path d="M2 0.5 L4 3 L3 4 Q4.5 6 6 7 L7 6 L9.5 8 L8 9.5 Q3 9 0.5 2 Z" fill="#1c4795"/></svg> (555) 214-7200</div>
      <div><svg class="icon" viewBox="0 0 10 10"><rect x="2.5" y="0.5" width="5" height="3" fill="#1c4795"/><rect x="0.5" y="3.5" width="9" height="4" fill="#1c4795"/><rect x="2.5" y="6.5" width="5" height="3" fill="#1c4795"/></svg> (555) 214-7300</div>
    </div>
    <div class="contact-block web">
      <div><svg class="icon" viewBox="0 0 10 10"><rect x="0.5" y="2" width="9" height="6" fill="#1c4795"/><path d="M0.5 2 L5 5.5 L9.5 2" stroke="#fff" fill="none"/></svg> info@quillfernlc.com</div>
      <div><svg class="icon" viewBox="0 0 10 10"><circle cx="5" cy="5" r="4.5" fill="#1c4795"/><path d="M0.5 5 H9.5 M5 0.5 V9.5" stroke="#fff" stroke-width=".7"/></svg> www.quillfernlc.com</div>
    </div>

    <div class="ghost-name">QUILLFERN<br>LITIGATION FUNDING</div>

    <div class="footer-band">
      <div class="band-main">Linden Court - Upper Level, 4810 Alder Avenue, Suite 620, Springfield, Ohio, 45502</div>
      <div class="band-mark"></div>
      <div class="band-end"></div>
    </div>
  </section>
</div>
</body>
</html>
```